Clinical Layout Builders - Stationery
Biz Cards + Stationary
Clinical Layout Builders - Stationery - Information Technology
Creative Brief
Professional
Dr. Elena M. Castillo
Director of Content Development
Ceiba Business Plaza #3, Suite 118 San Juan, PR 00941
(787) PENDING
elena.castillo@hnvwqbt.com
www.hnvwqbt.com
Need a second set of cards for: Dr. Luis F. Beltran Business Development Director Same info- address, fax and phone (Pending) Cell: (787) 555-0192 Email: luis.beltran@hnvwqbt.com
Either the logo, the website or something else. Feel free to be creative!

```html
<!DOCTYPE html>
<html lang="en">
<head>
<meta charset="utf-8">
<title>Clinical Layout Builders - Stationery</title>
<link rel="stylesheet" href="https://fonts.googleapis.com/css2?family=Roboto:wght@400;700;900&display=swap">
<style>
:root{
  --stage:#d8d9da;
  --paper:#ffffff;
  --magenta:#c2137c;
  --magenta-light:#e24aa3;
  --magenta-dark:#7d0a4f;
  --ink:#222226;
  --grey:#8e8f93;
  --grey-light:#c9cacc;
  --black:#111113;
  --shadow:0 2px 6px rgba(0,0,0,.22);
}
*{box-sizing:border-box;margin:0;padding:0}
html,body{width:1200px;height:710px;overflow:hidden}
body{background:var(--stage);font-family:"Roboto",Arial,sans-serif;color:var(--ink);position:relative}
.piece{position:absolute;background:var(--paper);box-shadow:var(--shadow);overflow:hidden}
.swoosh{position:absolute;left:0;top:0;width:100%}
.brand{position:absolute;font-weight:900;color:var(--ink);letter-spacing:.04em;line-height:1}
.brand-tag{position:absolute;font-size:5px;color:var(--grey);text-transform:uppercase;letter-spacing:.06em;white-space:nowrap}
.ghost{position:absolute;font-weight:900;color:var(--magenta);opacity:.12;letter-spacing:.04em;line-height:1}
.footer{position:absolute;left:0;right:0;text-align:center;font-size:5px;color:var(--grey);line-height:1.6}
.footer-row{display:flex;justify-content:space-between;padding:0 14px}

/* letterheads */
.sheet{top:103px;width:326px;height:526px}
.sheet-fax{left:41px}
.sheet-letter{left:396px}
.sheet .swoosh{height:84px}
.sheet .brand-tag{left:16px;top:37px}
.sheet .brand{left:16px;top:46px;font-size:26px}
.sheet .ghost{left:50%;transform:translateX(-50%);top:420px;font-size:46px}
.sheet .footer{bottom:12px}

.fax-title{position:absolute;right:16px;top:100px;font-size:15px;font-weight:900}
.fax-table{position:absolute;left:14px;top:118px;border-collapse:collapse;font-size:6px;width:296px}
.fax-table td{border:1.5px solid var(--black);height:13px;padding:0 3px}
.fax-table td.label{width:36px;font-weight:700}
.fax-table td.field{width:112px}
.fax-checks{position:absolute;left:14px;right:16px;top:178px;display:flex;justify-content:space-between;font-size:6px;font-weight:700}
.fax-checks span::before{content:"";display:inline-block;width:6px;height:6px;background:var(--black);margin-right:3px;vertical-align:-1px}

/* cards */
.card{top:31px;width:139px;height:72px}
.card-front{left:600px}
.card-back{left:758px;background:var(--black)}
.card .swoosh{height:40px}
.card .brand{left:8px;top:22px;font-size:12px}
.card-back .brand{left:50%;transform:translateX(-50%);top:30px;color:var(--paper)}
.card-person{position:absolute;right:6px;top:4px;text-align:right;font-size:4.2px;color:var(--paper);line-height:1.3;white-space:nowrap}
.card-person strong{display:block;font-size:5.6px}
.card-details{position:absolute;left:62px;top:40px;font-size:4.4px;line-height:1.5;color:var(--ink);white-space:nowrap}
.card-details li{list-style:none}
.card-details li::before{content:"";display:inline-block;width:3px;height:3px;background:var(--magenta);margin-right:2px}
.card-web{position:absolute;left:0;right:0;bottom:8px;text-align:center;font-size:4.5px;color:var(--magenta-light)}

/* compliment slip */
.slip{left:751px;top:144px;width:372px;height:211px}
.slip .swoosh{height:64px}
.slip .brand-tag{left:12px;top:27px}
.slip .brand{left:12px;top:35px;font-size:22px}
.slip .ghost{left:180px;top:160px;font-size:34px}
.slip .footer-row{position:absolute;left:0;right:0;top:92px;font-size:5px;color:var(--grey)}

/* envelopes */
.envelope{width:340px;height:178px}
.env-flap{left:696px;top:355px}
.env-flap svg{position:absolute;inset:0;width:100%;height:100%}
.env-flap .brand-tag{left:50%;transform:translateX(-50%);top:10px}
.env-dark{left:744px;top:420px;height:170px;width:331px}
.env-dark .dark-panel{position:absolute;left:0;right:0;top:0;height:74px;background:var(--black)}
.env-dark .brand{left:50%;transform:translateX(-50%);top:24px;font-size:22px;color:var(--paper)}
.env-dark .dark-tag{position:absolute;left:0;right:0;top:52px;text-align:center;font-size:5px;color:var(--grey-light)}
.env-pink{left:792px;top:480px;height:180px;width:341px}
.env-pink .pink-band{position:absolute;left:0;right:0;top:0;height:40px;background:linear-gradient(90deg,var(--magenta-dark),var(--magenta),var(--magenta-light),var(--magenta),var(--magenta-dark))}
.env-pink .band-text{position:absolute;left:0;right:0;top:18px;text-align:center;font-size:5px;color:var(--paper);letter-spacing:.05em}
</style>
</head>
<body>

<svg width="0" height="0" style="position:absolute" aria-hidden="true">
  <defs>
    <linearGradient id="pink" x1="0" x2="1" y1="0" y2="0">
      <stop offset="0" stop-color="#7d0a4f"/>
      <stop offset=".55" stop-color="#c2137c"/>
      <stop offset="1" stop-color="#e24aa3"/>
    </linearGradient>
    <symbol id="swoosh" viewBox="0 0 100 30" preserveAspectRatio="none">
      <path d="M0 0H100V28Q62 10 0 8Z" fill="url(#pink)"/>
      <path d="M0 10Q60 13 100 30" fill="none" stroke="#8e8f93" stroke-width="1.2"/>
    </symbol>
  </defs>
</svg>

<section class="piece sheet sheet-fax">
  <svg class="swoosh" aria-hidden="true"><use href="#swoosh"/></svg>
  <div class="brand-tag">Clinical Layout Builders</div>
  <div class="brand">HNVWQBT</div>
  <div class="fax-title">FAX</div>
  <table class="fax-table">
    <tr><td class="label">To:</td><td class="field"></td><td class="label">From:</td><td class="field"></td></tr>
    <tr><td class="label">Fax:</td><td class="field"></td><td class="label">Pages:</td><td class="field"></td></tr>
    <tr><td class="label">Phone:</td><td class="field"></td><td class="label">Date:</td><td class="field"></td></tr>
    <tr><td class="label">Re:</td><td class="field"></td><td class="label">CC:</td><td class="field"></td></tr>
  </table>
  <div class="fax-checks">
    <span>Urgent</span><span>For Review</span><span>Please Comment</span><span>Please Reply</span><span>Please Recycle</span>
  </div>
  <div class="ghost">HNVWQBT</div>
  <div class="footer">
    Ceiba Business Plaza #3, Suite 118 San Juan, PR 00941
    <div class="footer-row"><span>(787) 555-0192</span><span>elena.castillo@hnvwqbt.com</span><span>www.hnvwqbt.com</span></div>
  </div>
</section>

<section class="piece sheet sheet-letter">
  <svg class="swoosh" aria-hidden="true"><use href="#swoosh"/></svg>
  <div class="brand-tag">Clinical Layout Builders</div>
  <div class="brand">HNVWQBT</div>
  <div class="ghost">HNVWQBT</div>
  <div class="footer">
    Ceiba Business Plaza #3, Suite 118 San Juan, PR 00941
    <div class="footer-row"><span>(787) 555-0192</span><span>elena.castillo@hnvwqbt.com</span><span>www.hnvwqbt.com</span></div>
  </div>
</section>

<section class="piece card card-front">
  <svg class="swoosh" aria-hidden="true"><use href="#swoosh"/></svg>
  <div class="card-person"><strong>Dr. Elena M. Castillo</strong>Director of Content Development</div>
  <div class="brand">HNVWQBT</div>
  <ul class="card-details">
    <li>Ceiba Business Plaza #3, Suite 118</li>
    <li>San Juan, PR 00941</li>
    <li>(787) 555-0192</li>
    <li>elena.castillo@hnvwqbt.com</li>
  </ul>
</section>

<section class="piece card card-back">
  <div class="brand">HNVWQBT</div>
  <div class="card-web">www.hnvwqbt.com</div>
</section>

<section class="piece slip">
  <svg class="swoosh" aria-hidden="true"><use href="#swoosh"/></svg>
  <div class="brand-tag">Clinical Layout Builders</div>
  <div class="brand">HNVWQBT</div>
  <div class="footer-row"><span>(787) 555-0192</span><span>elena.castillo@hnvwqbt.com</span><span>www.hnvwqbt.com</span></div>
  <div class="ghost">HNVWQBT</div>
</section>

<section class="piece envelope env-flap">
  <svg viewBox="0 0 340 178" preserveAspectRatio="none" aria-hidden="true">
    <path d="M0 0L170 70L340 0" fill="none" stroke="#c9cacc" stroke-width="1"/>
  </svg>
  <div class="brand-tag">Ceiba Business Plaza #3, Suite 118 San Juan, PR 00941</div>
</section>

<section class="piece envelope env-dark">
  <div class="dark-panel"></div>
  <div class="brand">HNVWQBT</div>
  <div class="dark-tag">Clinical Layout Builders</div>
</section>

<section class="piece envelope env-pink">
  <div class="pink-band"></div>
  <div class="band-text">Ceiba Business Plaza #3, Suite 118 San Juan, PR 00941</div>
</section>

</body>
</html>
```